Corp Deck - Kestrel Lane Nursing

Kestrel Lane Nursing is a home health care company based in Ontario, Canada. The company's core belief is that homecare should be the foundational element of healthcare, and that a significant change needs to happen in how healthcare is delivered. We call this “Wholehearted Wellness Indoors”.

Kestrel Lane Nursing helps people deal with chronic conditions, ageing, and medical recovery in their home. We ensure a unified, complete experience all the way from matching the optimal care and caregiver with the client, to being a trusted navigator, helping the client and their family deal with the complex healthcare system.

This wholehearted wellness indoors is not only less stressful, but also drives better health outcomes.

We have been working on updating the content of our corporate deck to align with our new brand design. In addition to incorporating our new brand elements, we would like to introduce new templates, including our updated colors (along with complementary ones), graphics, and more suitable fonts. There are 21 slides.

Target Market(s)

For this corporate deck, the target audience consists of potential investors, industry leaders, and recognized media figures who possess a solid understanding of the industry and are keen to learn more about our wholehearted wellness indoors. These individuals are well-versed in the industry and expect presentations that stand out and capture their attention effectively. They typically have a high level of education.

Industry/Entity Type

Healthcare

Requirements
Must have
• Align the design with the new company's branding (see it on our website www.kestrellanenursing.example) emphasizing the vision of home care as the foundation of healthcare. Utilize a clean, modern design aesthetic that communicates trustworthiness, empathy, and professionalism. Incorporate the company's branding color palette and supplement it with hues that evoke feelings of trust, comfort, and reliability.
Nice to have
• Shapes, graphics, images that capture the essence of our wholehearted wellness indoors. Emphasize the human aspect of home health care.
Should not have
• Shapes, graphics, images, that infantilize older people or disrespect their dignity.

```html
<!DOCTYPE html>
<html lang="en">
<head>
<meta charset="utf-8">
<title>Kestrel Lane Nursing – Corporate Deck</title>
<link href="https://fonts.googleapis.com/css2?family=Playfair+Display:wght@400;700&family=Roboto:wght@400;500;700&display=swap" rel="stylesheet">
<style>
:root{
  --green:#46a01e;
  --green-dark:#3a8a17;
  --charcoal:#4a4a4a;
  --ink:#2b2b2b;
  --body:#444;
  --canvas:#e6e6e6;
  --white:#fff;
}
*{margin:0;padding:0;box-sizing:border-box}
html,body{width:1200px;height:3966px;overflow:hidden;background:var(--canvas)}
body{position:relative;font-family:'Roboto',sans-serif;color:var(--body)}
.slide{position:absolute;left:86px;width:1029px;height:579px;background:var(--white);overflow:hidden;box-shadow:0 2px 8px rgba(0,0,0,.08)}
.slide svg.deco{position:absolute;left:0;top:0;width:1029px;height:579px}
.brand{position:absolute;font-family:'Playfair Display',serif;font-weight:400;color:var(--white);font-size:30px;display:flex;align-items:center;gap:10px;white-space:nowrap}
.brand .dot{width:14px;height:14px;border-radius:50%;background:var(--white);flex:none}
.rule{position:absolute;height:3px;width:30px;background:var(--green)}
.checklist{position:absolute;list-style:none}
.checklist li{position:relative;padding-left:30px;font-size:17px;line-height:29px;color:#333}
.checklist li svg{position:absolute;left:0;top:calc(50% - 8px);width:16px;height:16px}
/* slide 1 */
.s1{top:86px}
.s1 .kicker{position:absolute;left:62px;top:468px;font-family:'Playfair Display',serif;font-weight:700;color:var(--green);font-size:28px}
.s1 .title{position:absolute;left:62px;top:506px;font-family:'Playfair Display',serif;font-weight:700;color:#555;font-size:42px;white-space:nowrap}
/* slide 2 */
.s2{top:729px}
.s2 h2{position:absolute;left:0;width:100%;top:292px;text-align:center;font-family:'Playfair Display',serif;font-weight:700;color:var(--ink);font-size:54px}
.s2 p{position:absolute;left:130px;width:769px;top:374px;text-align:center;font-size:31px;line-height:44px;color:#222}
/* slide 3 */
.s3{top:1373px}
.s3 h2{position:absolute;left:590px;top:56px;font-family:'Playfair Display',serif;font-weight:700;color:var(--ink);font-size:33px;line-height:37px}
.s3 .checklist{left:590px;top:160px;width:400px}
.s3 .checklist li{text-align:justify;margin-bottom:14px}
/* slide 4 */
.s4{top:2016px}
.driver{position:absolute;top:185px;width:200px;text-align:center}
.driver .badge{width:116px;height:116px;border-radius:50%;margin:0 auto;display:flex;align-items:center;justify-content:center;box-shadow:0 3px 6px rgba(0,0,0,.25)}
.driver .badge.green{background:var(--green)}
.driver .badge.dark{background:var(--charcoal)}
.driver h3{font-size:15px;font-weight:700;color:#222;margin-top:20px;line-height:19px}
.driver p{font-size:15px;line-height:22px;color:#333;margin-top:20px}
/* slide 5 */
.s5{top:2659px}
.s5 h2{position:absolute;left:62px;top:160px;font-family:'Playfair Display',serif;font-weight:700;color:var(--ink);font-size:33px}
.s5 .checklist{left:62px;top:226px;width:452px}
.s5 .checklist li{margin-bottom:4px}
/* slide 6 */
.s6{top:3303px;background:var(--green)}
.s6 h2{position:absolute;left:0;width:100%;top:262px;text-align:center;font-family:'Playfair Display',serif;font-weight:700;color:var(--white);font-size:60px;line-height:66px}
</style>
</head>
<body>

<section class="slide s1">
  <svg class="deco" viewBox="0 0 1029 579">
    <defs><linearGradient id="g1" x1="0" y1="0" x2="1" y2="1"><stop offset="0" stop-color="#a9c796"/><stop offset="1" stop-color="#7faa63"/></linearGradient></defs>
    <rect width="1029" height="420" fill="url(#g1)" role="img" aria-label="Caregiver sitting with an elderly woman in a bright living room"/>
    <path d="M0,330 C40,470 250,480 1029,300 L1029,579 L0,579Z" fill="var(--white)"/>
    <path d="M0,330 C40,455 250,460 1029,300 C300,480 60,500 0,360Z" fill="var(--charcoal)"/>
  </svg>
  <div class="brand" style="right:50px;top:50px;font-size:28px"><span class="dot"></span>Kestrel Lane Nursing</div>
  <div class="kicker">Welcome To</div>
  <div class="title">Kestrel Lane Nursing Care Services</div>
</section>

<section class="slide s2">
  <svg class="deco" viewBox="0 0 1029 579">
    <defs><linearGradient id="g2" x1="0" y1="0" x2="1" y2="0"><stop offset="0" stop-color="#f1efec"/><stop offset="1" stop-color="#e9ece9"/></linearGradient></defs>
    <rect width="1029" height="579" fill="url(#g2)" role="img" aria-label="Nurse checking an elderly woman's blood pressure at home"/>
    <path d="M0,0 H1029 V40 C700,50 300,60 120,95 C60,105 20,80 0,55Z" fill="var(--green)"/>
    <path d="M80,85 C180,150 500,110 830,75 C500,120 280,150 180,140 C130,135 95,115 80,85Z" fill="var(--charcoal)"/>
  </svg>
  <div class="brand" style="left:62px;top:22px"><span class="dot"></span>Kestrel Lane Nursing</div>
  <h2>Capability Statement</h2>
  <p>No, because the model has never been accurately defined, or described</p>
</section>

<section class="slide s3">
  <svg class="deco" viewBox="0 0 1029 579">
    <rect x="0" y="0" width="553" height="579" fill="var(--green)"/>
    <path d="M260,0 H553 V579 H300 C280,470 200,420 230,300 C250,200 200,90 260,0Z" fill="#e4ddd6" role="img" aria-label="Young woman embracing a smiling elderly woman in a wheelchair"/>
    <path d="M260,0 C200,90 250,200 230,300 C200,420 280,470 300,579 L292,579 C270,470 190,420 220,300 C240,200 190,90 250,0Z" fill="var(--charcoal)"/>
  </svg>
  <div class="brand" style="left:62px;top:512px;font-size:26px"><span class="dot"></span>Kestrel Lane</div>
  <h2>Around the<br>World: Denmark</h2>
  <div class="rule" style="left:590px;top:138px"></div>
  <ul class="checklist">
    <li><svg viewBox="0 0 16 16"><circle cx="8" cy="8" r="8" fill="var(--green)"/><path d="M4.5,8.2 7,10.6 11.5,5.8" stroke="#fff" stroke-width="2" fill="none"/></svg>Senior Friendly system with principles of self- reliance, dignity and self-respect, integrated into the community</li>
    <li><svg viewBox="0 0 16 16"><circle cx="8" cy="8" r="8" fill="var(--green)"/><path d="M4.5,8.2 7,10.6 11.5,5.8" stroke="#fff" stroke-width="2" fill="none"/></svg>National strategy to maintain people in their homes. In the 1980's legislated against the building of any new LTC homes</li>
    <li><svg viewBox="0 0 16 16"><circle cx="8" cy="8" r="8" fill="var(--green)"/><path d="M4.5,8.2 7,10.6 11.5,5.8" stroke="#fff" stroke-width="2" fill="none"/></svg>Patient outcomes tracked, with funded nursing and caregiving under universal health insurance</li>
    <li><svg viewBox="0 0 16 16"><circle cx="8" cy="8" r="8" fill="var(--green)"/><path d="M4.5,8.2 7,10.6 11.5,5.8" stroke="#fff" stroke-width="2" fill="none"/></svg>Best outcomes and satisfaction levels of any OECD country</li>
  </ul>
</section>

<section class="slide s4">
  <svg class="deco" viewBox="0 0 1029 579">
    <path d="M0,0 H1029 V40 C700,50 300,60 120,95 C60,105 20,80 0,55Z" fill="var(--green)"/>
    <path d="M80,85 C180,150 500,110 830,75 C500,120 280,150 180,140 C130,135 95,115 80,85Z" fill="var(--charcoal)"/>
  </svg>
  <div class="brand" style="left:62px;top:22px"><span class="dot"></span>Kestrel Lane Nursing</div>
  <div class="driver" style="left:52px">
    <div class="badge green"><svg width="44" height="56" viewBox="0 0 44 56" fill="#fff"><circle cx="20" cy="7" r="6"/><path d="M14,16 H26 L30,36 H24 L24,54 H19 L19,40 H17 L17,54 H12 V36 H8Z"/><rect x="32" y="26" width="3" height="28"/></svg></div>
    <h3>Rising Geriatric<br>Population</h3>
    <p>6.2 mill CDN's 65 and over will rise to 10.4 mill by 2037.<br><br>7 out of 10 will need long-term care support.</p>
  </div>
  <div class="driver" style="left:294px">
    <div class="badge dark"><svg width="52" height="56" viewBox="0 0 52 56" fill="none" stroke="#fff" stroke-width="4"><circle cx="20" cy="6" r="4" fill="#fff" stroke="none"/><path d="M20,14 V30 H34 L40,44 H46"/><path d="M14,24 A14,14 0 1 0 34,40"/></svg></div>
    <h3>Increasing Chronic<br>Conditions</h3>
    <p>Notably dementia and Alzheimer's.<br><br>13.7% of CDN's have a disability.</p>
  </div>
  <div class="driver" style="left:536px">
    <div class="badge green"><svg width="60" height="60" viewBox="0 0 60 60" fill="#fff" stroke="#fff" stroke-width="3"><circle cx="30" cy="30" r="14"/><path d="M30,6 V14 M30,46 V54 M6,30 H14 M46,30 H54 M13,13 19,19 M41,41 47,47 M47,13 41,19 M13,47 19,41"/></svg></div>
    <h3>Covid Reverberations<br>and Change</h3>
    <p>Covid impact still being felt.<br><br>Much change is permanent.</p>
  </div>
  <div class="driver" style="left:778px">
    <div class="badge dark"><svg width="40" height="60" viewBox="0 0 40 60" fill="none" stroke="#fff" stroke-width="3"><rect x="4" y="3" width="32" height="54" rx="4"/><circle cx="14" cy="22" r="3"/><circle cx="26" cy="32" r="3"/><circle cx="14" cy="42" r="3"/><path d="M16,24 24,30 M24,34 16,40"/></svg></div>
    <h3>Digital Inflection Point</h3>
    <p style="font-size:14px;line-height:21px">HealthTech / Mobile Back-end efficiencies<br>Behavioral:<br>- Less than 40% of CDN's have accessed HC records online. But 4 out 5 CDN's want to use online HC resources</p>
  </div>
</section>

<section class="slide s5">
  <svg class="deco" viewBox="0 0 1029 579">
    <path d="M0,0 H1029 V40 C700,50 300,60 120,95 C60,105 20,80 0,55Z" fill="var(--green)"/>
    <path d="M80,85 C180,150 500,110 830,75 C500,120 280,150 180,140 C130,135 95,115 80,85Z" fill="var(--charcoal)"/>
    <circle cx="758" cy="360" r="208" fill="var(--green-dark)"/>
    <circle cx="758" cy="360" r="196" fill="var(--charcoal)"/>
    <circle cx="750" cy="360" r="188" fill="#8a6d5c" role="img" aria-label="Caregiver sharing a moment with an elderly woman at a table"/>
  </svg>
  <div class="brand" style="left:62px;top:22px"><span class="dot"></span>Kestrel Lane Nursing</div>
  <h2>Key Industry Drivers</h2>
  <div class="rule" style="left:62px;top:208px"></div>
  <ul class="checklist">
    <li><svg viewBox="0 0 16 16"><circle cx="8" cy="8" r="8" fill="var(--green)"/><path d="M4.5,8.2 7,10.6 11.5,5.8" stroke="#fff" stroke-width="2" fill="none"/></svg>Health Care in Canada (public) was $331bn in 2022. Only 3.8% of that, ($12.5bn) was for home and community care</li>
    <li><svg viewBox="0 0 16 16"><circle cx="8" cy="8" r="8" fill="var(--green)"/><path d="M4.5,8.2 7,10.6 11.5,5.8" stroke="#fff" stroke-width="2" fill="none"/></svg>Private care represents about 25% of the total, suggesting that home care provider industry in 2022 was about $16bn</li>
    <li><svg viewBox="0 0 16 16"><circle cx="8" cy="8" r="8" fill="var(--green)"/><path d="M4.5,8.2 7,10.6 11.5,5.8" stroke="#fff" stroke-width="2" fill="none"/></svg>There were 4,295 businesses in this category, with the vast majority doing $1-3m in annual revenue (owner operated)</li>
    <li><svg viewBox="0 0 16 16"><circle cx="8" cy="8" r="8" fill="var(--green)"/><path d="M4.5,8.2 7,10.6 11.5,5.8" stroke="#fff" stroke-width="2" fill="none"/></svg>Carewell Home Health was the top company by revenue with about $440.3m in this area (home health care),</li>
  </ul>
</section>

<section class="slide s6">
  <svg class="deco" viewBox="0 0 1029 579">
    <defs><radialGradient id="g6" cx=".62" cy=".45" r=".6"><stop offset="0" stop-color="#5aa833"/><stop offset="1" stop-color="var(--green)"/></radialGradient></defs>
    <rect width="1029" height="579" fill="url(#g6)" role="img" aria-label="Faint image of a caregiver with an older client"/>
  </svg>
  <div class="brand" style="left:62px;top:40px;font-size:34px"><span class="dot"></span>Kestrel Lane Nursing</div>
  <h2>Delivering Comprehensive<br>Health@Home</h2>
</section>

</body>
</html>
```